Antibacterial Hand Wash Squeeze Tube Label

We're looking for a contemporary label design for a new Antibacterial Hand Wash for an 8oz squeeze tube. The new consumer brand will be sold to consumers in major US retail stores & online. The moisturizing hand wash contains Aloe Vera, vitamin E, and other natural ingredients so the design should include the color green. Real photos are very effective on packaging, so a picture of Aloe Vera or possibly two hands washing would help draw consumers' attention to the tube on the retail shelf. The front label may wrap around the sides. Rear must be left mostly blank
US Consumers - retail stores & online
Consumer

```html
<!DOCTYPE html>
<html lang="en">
<head>
<meta charset="utf-8">
<title>Antibacterial Hand Sanitizer Tube Label</title>
<link rel="stylesheet" href="https://fonts.googleapis.com/css2?family=Montserrat:wght@400;500;600;700&family=PT+Sans:ital,wght@1,700&family=Noto+Serif:ital@1&display=swap">
<style>
  :root {
    --page: #ffffff;
    --green: #7cc242;
    --green-deep: #3aa535;
    --green-pale: #d9edb4;
    --green-mid: #b6dc7a;
    --brand-blue: #1a87c8;
    --red: #c8151b;
    --ink: #1d1d1b;
    --pill-light: #f4f4f4;
    --pill-dark: #bdbdbd;
  }
  * { margin: 0; padding: 0; box-sizing: border-box; }
  html, body {
    width: 1200px; height: 739px; overflow: hidden;
    background: var(--page);
  }
  .label-sheet {
    position: absolute; left: 289px; top: 20px;
    width: 623px; height: 700px;
    background: var(--page);
    box-shadow: 0 0 28px rgba(0,0,0,0.08);
  }
  .front-panel {
    position: absolute; left: 0; top: 0;
    width: 312px; height: 685px;
    overflow: hidden;
  }
  .panel-art { position: absolute; inset: 0; }
  .centered {
    position: absolute; left: 0; width: 312px; text-align: center;
  }
  .brand {
    top: 95px;
    display: flex; justify-content: center; align-items: center; gap: 6px;
    font-family: "Montserrat", sans-serif; font-weight: 700;
    font-size: 18px; line-height: 22px; color: var(--brand-blue);
  }
  .brand-mark {
    width: 16px; height: 16px; border-radius: 50%;
    background: var(--brand-blue);
  }
  .kicker {
    top: 164px;
    font-family: "Montserrat", sans-serif; font-weight: 500;
    font-size: 16px; line-height: 22px; letter-spacing: 3.6px; color: var(--green-deep);
  }
  .product-name {
    top: 182px;
    font-family: "PT Sans", sans-serif; font-style: italic; font-weight: 700;
    color: var(--green-deep); line-height: 44px;
    text-shadow: 1px 1px 0 #cfe8b6;
  }
  .product-name .line {
    display: block; font-size: 51px; letter-spacing: -0.5px;
  }
  .variant-pill {
    position: absolute; left: 61px; top: 281px;
    width: 190px; height: 22px; border-radius: 6px;
    background: linear-gradient(90deg, var(--pill-dark), var(--pill-light) 30%, var(--pill-light) 70%, var(--pill-dark));
    font-family: "Montserrat", sans-serif; font-weight: 500;
    font-size: 14px; line-height: 22px; letter-spacing: 0.5px;
    text-align: center; color: var(--ink);
  }
  .claim {
    top: 319px;
    font-family: "Noto Serif", serif; font-style: italic;
    font-size: 15px; line-height: 15px; color: var(--red);
  }
  .ingredients {
    top: 382px;
    font-family: "Montserrat", sans-serif; font-weight: 700;
    font-size: 19px; line-height: 22px; color: var(--green-deep);
  }
  .ingredients-note {
    top: 427px;
    font-family: "Montserrat", sans-serif; font-weight: 400;
    font-size: 9.5px; line-height: 12px; color: var(--green-deep);
  }
  .net-weight {
    position: absolute; left: 238px; top: 636px;
    font-family: "Montserrat", sans-serif; font-weight: 500;
    font-size: 20px; line-height: 24px; color: var(--ink);
  }
</style>
</head>
<body>
  <div class="label-sheet">
    <div class="front-panel">
      <svg class="panel-art" width="312" height="685" viewBox="0 0 312 685" aria-hidden="true">
        <defs>
          <linearGradient id="bandFill" x1="0" y1="0" x2="0" y2="1">
            <stop offset="0" stop-color="#a8d46a"/>
            <stop offset="1" stop-color="#bfe07f"/>
          </linearGradient>
          <linearGradient id="silverSwoosh" x1="0" y1="0" x2="1" y2="0">
            <stop offset="0" stop-color="#d8d8d8"/>
            <stop offset="1" stop-color="#ffffff"/>
          </linearGradient>
          <radialGradient id="photoTone" cx="0.6" cy="0.55" r="0.6">
            <stop offset="0" stop-color="#6cbf3c"/>
            <stop offset="0.7" stop-color="#9fd36a" stop-opacity="0.7"/>
            <stop offset="1" stop-color="#c9e6a0" stop-opacity="0"/>
          </radialGradient>
        </defs>
        <path d="M0 128 L0 74 Q0 60 14 60 L203 60 Q80 72 0 128 Z" fill="var(--green)"/>
        <path d="M0 146 Q60 82 203 60 Q92 84 12 152 Z" fill="url(#silverSwoosh)"/>
        <path d="M0 495 Q110 530 312 470 L312 685 L0 685 Z" fill="var(--green)"/>
        <path d="M0 505 Q110 545 312 480 L312 500 Q140 560 0 545 Z" fill="#e2e2e2"/>
        <path d="M0 540 Q150 565 312 500 L312 685 L0 685 Z" fill="url(#bandFill)"/>
        <path d="M0 575 Q150 570 312 530 L312 560 Q150 600 0 610 Z" fill="var(--green-pale)" opacity="0.6"/>
        <rect x="66" y="455" width="246" height="180" fill="url(#photoTone)"
              role="img" aria-label="Photo of sliced aloe vera leaves above cupped lathered hands"/>
      </svg>

      <div class="centered brand"><span class="brand-mark"></span>Hollenby</div>
      <div class="centered kicker">ANTIBACTERIAL</div>
      <h1 class="centered product-name"><span class="line">HAND</span><span class="line">SANITIZER</span></h1>
      <div class="variant-pill">MOISTURIZING</div>
      <p class="centered claim">Kills<br>99.9% of<br>Germs</p>
      <p class="centered ingredients">ALOE VERA<br>VITAMIN E</p>
      <p class="centered ingredients-note">OTHER NATURAL INGREDIENTS</p>
      <p class="net-weight">8 oz</p>
    </div>
  </div>
</body>
</html>
```